Law Firm Stationery Design - Traditional Meets Intuitive

Looking for a modern, yet classic, law firm stationery design. Simplicity is desired, but great ideas are encouraged. See attachment for company information. We utilize a variety of non-traditional legal tools to bring a different perspective to each of our client's particular situation. Final design should communicate classic values with intuitive, unique solutions.

Industry/Entity Type

Law Firm

Requirements
Should not have
• - No typical legal icons
• - No Tag Line!
• - DO NOT WANT WHAT WE ALREADY HAVE

```html
<!DOCTYPE html>
<html lang="en">
<head>
<meta charset="utf-8">
<title>Veritan Law LLC — Stationery</title>
<link href="https://fonts.googleapis.com/css2?family=Tinos:wght@400;700&display=swap" rel="stylesheet">
<style>
  :root{
    --bg:#dedede;
    --charcoal:#2a2a2a;
    --charcoal-deep:#1f1f1f;
    --paper:#ffffff;
    --gold:#c8901c;
    --gold-light:#e2b04a;
    --gold-dark:#a8720e;
    --ink:#1c1c1c;
    --muted:#6b6b6b;
    --rule:#c9c9c9;
  }
  *{box-sizing:border-box;margin:0;padding:0}
  html,body{width:855px;height:1200px;overflow:hidden}
  body{background:var(--bg);font-family:"Tinos",serif;color:var(--ink);position:relative}

  .piece{position:absolute;overflow:hidden}
  .brand{font-family:"Tinos",serif;font-weight:400;color:var(--gold);white-space:nowrap;display:flex;align-items:center}
  .brand .mark{display:inline-block;flex:none;background:var(--gold)}
  .brand .words{display:flex;flex-direction:column;align-items:center;line-height:1}
  .brand .words .sub{font-size:.72em;margin-top:.12em}

  .band{position:absolute;left:0;right:0;bottom:0}
  .band .strip{position:absolute;left:0;right:0;bottom:0;background:var(--charcoal)}
  .band .accent{position:absolute;right:0;bottom:0;height:100%;
    background:linear-gradient(90deg,var(--gold-dark),var(--gold-light) 55%,var(--gold));
    clip-path:polygon(14% 0,100% 0,100% 100%,0 100%)}

  /* folder */
  .folder{left:46px;top:73px;width:294px;height:461px;background:var(--charcoal)}
  .folder .brand{position:absolute;left:40px;top:212px;font-size:30px}

  /* letterhead */
  .letterhead{left:217px;top:98px;width:262px;height:378px;background:var(--paper);box-shadow:0 2px 6px rgba(0,0,0,.25)}
  .letterhead .brand{position:absolute;left:14px;top:11px;font-size:10px;gap:4px}
  .letterhead .brand .mark{width:9px;height:9px}
  .letterhead .top-rule{position:absolute;left:14px;top:34px;width:60px;height:1px;background:var(--gold)}
  .letterhead .contact{position:absolute;right:14px;top:11px;font-size:3.6px;line-height:5px;color:var(--muted);width:58px}
  .letterhead .letter{position:absolute;left:14px;top:58px;width:230px;font-size:5.4px;line-height:6.6px;color:var(--ink)}
  .letterhead .letter p{margin-bottom:5px}
  .letterhead .band{height:9px}
  .letterhead .band .strip{height:4px}
  .letterhead .band .accent{width:62px}

  /* small business cards */
  .card-back-sm{left:553px;top:187px;width:84px;height:48px;background:var(--charcoal)}
  .card-back-sm .brand{position:absolute;left:0;right:0;top:19px;justify-content:center;font-size:8px}
  .card-front-sm{left:650px;top:187px;width:116px;height:48px;background:var(--paper);box-shadow:0 1px 3px rgba(0,0,0,.2)}
  .card-front-sm .brand{position:absolute;left:6px;top:14px;font-size:6px;gap:2px}
  .card-front-sm .brand .mark{width:5px;height:5px}
  .card-front-sm .info{position:absolute;left:62px;top:9px;font-size:3px;line-height:4px;color:var(--muted)}
  .card-front-sm .info .name{color:var(--gold);font-weight:700;font-size:4px}
  .card-front-sm .band{height:5px}
  .card-front-sm .band .strip{height:2px}
  .card-front-sm .band .accent{width:30px}

  /* envelope */
  .envelope{left:515px;top:248px;width:252px;height:84px;background:var(--paper);box-shadow:0 1px 3px rgba(0,0,0,.2)}
  .envelope svg{position:absolute;left:0;top:0}
  .envelope .flap-mark{position:absolute;left:120px;top:12px;width:12px;height:12px;background:var(--gold)}

  /* compliment slip */
  .slip{left:515px;top:342px;width:252px;height:132px;background:var(--paper);box-shadow:0 1px 3px rgba(0,0,0,.2)}
  .slip .brand{position:absolute;left:14px;top:14px;font-size:10px;gap:4px}
  .slip .brand .mark{width:9px;height:9px}
  .slip .return{position:absolute;left:14px;bottom:14px;font-size:3.8px;line-height:5px;color:var(--muted)}
  .slip .band{height:8px}
  .slip .band .strip{height:4px}
  .slip .band .accent{width:60px}

  /* large card back */
  .card-back{left:420px;top:580px;width:390px;height:228px;background:linear-gradient(160deg,#323232,var(--charcoal-deep))}
  .card-back .brand{position:absolute;left:0;right:0;top:96px;justify-content:center;font-size:30px;gap:12px}
  .card-back .brand .mark{width:22px;height:22px}

  /* large card front */
  .card-front{left:46px;top:840px;width:560px;height:320px;background:var(--paper);box-shadow:0 3px 10px rgba(0,0,0,.25)}
  .card-front .brand{position:absolute;left:44px;top:122px;font-size:28px;gap:12px}
  .card-front .brand .mark{width:22px;height:22px}
  .card-front .divider{position:absolute;left:288px;top:58px;width:1px;height:190px;background:var(--rule)}
  .card-front .details{position:absolute;left:308px;top:68px}
  .card-front .name{font-size:20px;font-weight:700;color:var(--gold);line-height:22px}
  .card-front .title{font-size:14px;color:var(--ink);margin-bottom:22px}
  .card-front .line{display:flex;align-items:flex-start;gap:8px;font-size:15px;line-height:19px;margin-bottom:4px}
  .card-front .line svg{flex:none;margin-top:3px}
  .card-front .band{height:24px}
  .card-front .band .strip{height:12px}
  .card-front .band .accent{width:150px}
</style>
</head>
<body>

  <div class="piece folder">
    <div class="brand">VERITAN</div>
  </div>

  <div class="piece letterhead">
    <div class="brand"><span class="mark"></span><span class="words"><span>VERITAN</span><span class="sub">LAW LLC</span></span></div>
    <div class="top-rule"></div>
    <div class="contact">
      VERITAN LAW LLC<br>
      18 Harbor Lane, Suite 300<br>
      Easton, MA 02375<br>
      Phone: 617-555-0142<br>
      www.veritanlaw.com
    </div>
    <div class="letter">
      <p>Dear Ms. Harlow:</p>
      <p>Nothing is as exciting as getting ready for game day.</p>
      <p>The players warming up, the buzz of the crowd as they enter the park, even the smell of the stadium, all make for an electrically charged atmosphere. I've seen it first hand, and I love it.</p>
      <p>I've been around professional sports since I was a child. My father worked as a league baseball scout for more than 35 years. Even more importantly, I had the pleasure of spending this past summer as an intern for the Riverton Rails minor league baseball team.</p>
      <p>It was an amazing experience. I interned in the Public/Media Relations department and had a chance to try my hand at an incredible variety of projects. I handled all our player appearances. I even set up and ran our first baseball camp. I usually put in 80 hours a week and couldn't get enough!</p>
      <p>That experience, in addition to work for the Lakeside Hawks and my Sports Management major, all have me extremely interested in pursuing a career in Sports Marketing upon graduation.</p>
      <p>I would love to talk with you more about my passion, my background, and your organization. I look forward to touching base with you soon.</p>
      <p>Regards,</p>
      <p>Maren Cole</p>
    </div>
    <div class="band"><div class="strip"></div><div class="accent"></div></div>
  </div>

  <div class="piece card-back-sm">
    <div class="brand">VERITAN</div>
  </div>

  <div class="piece card-front-sm">
    <div class="brand"><span class="mark"></span><span class="words"><span>VERITAN</span><span class="sub">LAW LLC</span></span></div>
    <div class="info">
      <div class="name">Daniel Reyes</div>
      President<br>
      18 Harbor Lane, Suite 300<br>
      Phone: 617-555-0142<br>
      www.veritanlaw.com
    </div>
    <div class="band"><div class="strip"></div><div class="accent"></div></div>
  </div>

  <div class="piece envelope">
    <svg width="252" height="84" viewBox="0 0 252 84" aria-hidden="true">
      <polygon points="0,0 252,0 252,10 134,44 118,44 0,10" fill="#2a2a2a"/>
    </svg>
    <div class="flap-mark"></div>
  </div>

  <div class="piece slip">
    <div class="brand"><span class="mark"></span><span class="words"><span>VERITAN</span><span class="sub">LAW LLC</span></span></div>
    <div class="return">
      If undelivered, please return to:<br>
      18 Harbor Lane, Suite 300 Easton, MA 02375
    </div>
    <div class="band"><div class="strip"></div><div class="accent"></div></div>
  </div>

  <div class="piece card-back">
    <div class="brand"><span class="mark"></span>VERITAN</div>
  </div>

  <div class="piece card-front">
    <div class="brand"><span class="mark"></span><span class="words"><span>VERITAN</span><span class="sub">LAW LLC</span></span></div>
    <div class="divider"></div>
    <div class="details">
      <div class="name">Daniel Reyes</div>
      <div class="title">President</div>
      <div class="line">
        <svg width="10" height="13" viewBox="0 0 10 13" aria-hidden="true"><path d="M5 0C2.2 0 0 2.2 0 5c0 3.6 5 8 5 8s5-4.4 5-8c0-2.8-2.2-5-5-5zm0 7a2 2 0 1 1 0-4 2 2 0 0 1 0 4z" fill="#c8901c"/></svg>
        <span>18 Harbor Lane, Suite 300<br>Easton, MA 02375</span>
      </div>
      <div class="line">
        <svg width="10" height="12" viewBox="0 0 10 12" aria-hidden="true"><rect x="1.5" y="0" width="7" height="12" rx="1.5" fill="#6b6b6b"/><rect x="3" y="1.5" width="4" height="7" fill="#fff"/></svg>
        <span>Phone: 617-555-0142</span>
      </div>
      <div class="line">
        <svg width="11" height="11" viewBox="0 0 11 11" aria-hidden="true"><circle cx="5.5" cy="5.5" r="5" fill="none" stroke="#c8901c" stroke-width="1.2"/><path d="M0.5 5.5h10M5.5 0.5c-2.6 2.8-2.6 7.2 0 10M5.5 0.5c2.6 2.8 2.6 7.2 0 10" fill="none" stroke="#c8901c" stroke-width="0.9"/></svg>
        <span>www.veritanlaw.com</span>
      </div>
    </div>
    <div class="band"><div class="strip"></div><div class="accent"></div></div>
  </div>

</body>
</html>
```